Brevora web site / landing page

Looking for design help with building a landing page for our company and possible the remaining site. We are an AI developer and customer software developer company. Uploading logos for color scheme attached in logo xip file.

Target Market(s)

Manufacturing, Small business, Sales

Coding

Coded - Design and coding required

Number of Pages Required

3 page

Colors

Designer to choose colors to be used in the design.

Requirements
Must have
• Landing page, additional pages for AI, Custom software and Customer Portals explanation.

```html
<!DOCTYPE html>
<html lang="en">
<head>
<meta charset="utf-8">
<title>Brevora — AI Integration &amp; Custom Software</title>
<link href="https://fonts.googleapis.com/css2?family=Open+Sans:wght@400;600;700&display=swap" rel="stylesheet">
<style>
:root{
  --navy:#14336b;
  --navy-deep:#0f2b5e;
  --navy-band:#173a78;
  --ink:#333333;
  --body:#4a4a4a;
  --muted:#777777;
  --grey-band:#e3e5e8;
  --charcoal:#333333;
  --white:#ffffff;
  --line:#9aa3b3;
}
*{box-sizing:border-box;margin:0;padding:0}
html,body{width:1200px;height:3351px;overflow:hidden}
body{position:relative;background:var(--white);font-family:"Open Sans",Arial,sans-serif;color:var(--body)}
.abs{position:absolute}

/* header */
.brand{left:110px;top:50px;font-size:22px;letter-spacing:9px;color:var(--navy);font-weight:400;display:flex;align-items:center;gap:12px}
.brand-dot{width:14px;height:14px;border-radius:50%;background:var(--navy)}
.nav{top:52px;font-size:18px;color:#777}
.nav.active{color:var(--navy);font-weight:700}
.nav-mark{left:413px;top:80px;width:52px;height:2px;background:#9aa3b3}
.nav-mark::after{content:"";position:absolute;left:23px;top:-2px;width:6px;height:6px;border-radius:50%;background:var(--navy)}

/* pill buttons */
.pill{height:47px;border-radius:24px;display:flex;align-items:center;padding-left:46px;font-size:16px;color:var(--white);position:absolute}
.pill::before{content:"";position:absolute;left:14px;top:14px;width:19px;height:19px;border-radius:50%;border:1px dotted rgba(255,255,255,.6)}
.pill::after{content:"";position:absolute;left:21px;top:21px;width:5px;height:5px;border-radius:50%;background:#8fb4e8}
.pill.navy{background:var(--navy)}
.pill.dark{background:var(--charcoal)}
.pill.outline{border:2px solid var(--white);background:transparent}

/* hero */
.hero{left:0;top:115px;width:1200px;height:660px}

/* section headings */
.eyebrow{font-size:16px;color:var(--navy);font-weight:600;letter-spacing:.3px}
.heading{font-size:32px;color:var(--ink);font-weight:400}
.heading b{font-weight:700}
.rule{height:1px;background:var(--line)}
.copy{font-size:15px;line-height:26.6px;color:var(--body)}

.photo{border-radius:40px;overflow:hidden}

/* services */
.services-band{left:0;top:1320px;width:1200px;height:747px;background:var(--grey-band)}
.section-title{width:1200px;text-align:center;font-size:31px;color:var(--ink)}
.section-title b{font-weight:700}
.title-rule{height:2px;background:var(--navy)}
.card{top:1475px;width:228px;height:508px;background:var(--white);border:1px solid #b9bec6}
.card-photo{height:221px}
.card h3{font-size:15px;font-weight:700;color:var(--ink);margin:25px 0 0 11px}
.card ul{list-style:none;margin:14px 8px 0 11px;font-size:12px;line-height:24px;color:var(--ink)}
.card li{padding-left:22px;position:relative}
.card li::before{content:"»";position:absolute;left:0;color:var(--navy);font-weight:700}
.card .more{position:absolute;left:10px;bottom:20px;font-size:14px;color:var(--navy)}

/* contact */
.contact-band{left:0;top:2607px;width:1200px;height:744px;background:linear-gradient(180deg,var(--navy-deep),var(--navy-band))}
.field{border:1px solid rgba(255,255,255,.75);color:rgba(255,255,255,.85);font-size:15px;padding:0 30px;display:flex;align-items:center}
.field.tall{align-items:flex-start;padding-top:20px}
.footer-text{left:0;width:1200px;top:3293px;text-align:center;font-size:16px;color:var(--white)}
</style>
</head>
<body>

<header>
  <div class="abs brand"><span class="brand-dot"></span>BREVORA</div>
  <span class="abs nav active" style="left:413px">Home</span>
  <span class="abs nav-mark"></span>
  <span class="abs nav" style="left:504px">Services</span>
  <span class="abs nav" style="left:610px">About Us</span>
  <span class="abs nav" style="left:723px">Contact</span>
  <a class="pill navy" style="left:873px;top:39px;width:215px">Customer Portals</a>
</header>

<svg class="abs hero" viewBox="0 0 1200 660" role="img" aria-label="Hand holding a smartphone with glowing AI network icons over a binary code backdrop">
  <defs>
    <linearGradient id="heroFill" x1="0" y1="0" x2="1" y2="1">
      <stop offset="0" stop-color="#2c5aa0"/>
      <stop offset=".5" stop-color="#4f7fc0"/>
      <stop offset="1" stop-color="#1d3f7a"/>
    </linearGradient>
  </defs>
  <path d="M0 0H1200V560Q600 760 0 560Z" fill="url(#heroFill)"/>
  <path d="M0 560Q600 760 1200 560V580Q600 780 0 580Z" fill="var(--navy-deep)"/>
</svg>

<section>
  <div class="abs photo" style="left:110px;top:858px;width:449px;height:355px;background:linear-gradient(135deg,#d8e2ec,#7f9fbf 55%,#3f6a98)" role="img" aria-label="Hands holding a tablet displaying AI interface graphics"></div>
  <div class="abs eyebrow" style="left:615px;top:862px">ABOUT US</div>
  <h2 class="abs heading" style="left:615px;top:888px"><b>Artificial Intelligence</b> With Results</h2>
  <div class="abs rule" style="left:615px;top:936px;width:473px"></div>
  <p class="abs copy" style="left:615px;top:952px;width:480px">At Brevora, we provide critical AI and automation systems that have dramatically increased efficiencies and profitability for our customers. We have established long term relationships with many companies in the aerospace, medical and finance industries, among others. Let us help your company automate tasks so that you can focus on growing your business. Contact us today for an on-site visit to get started reaping the benefits of AI.</p>
  <a class="pill navy" style="left:616px;top:1162px;width:203px">Custom software</a>
  <a class="pill dark" style="left:839px;top:1162px;width:201px">Contact Us Now</a>
</section>

<section>
  <div class="abs services-band"></div>
  <h2 class="abs section-title" style="left:0;top:1392px"><b>Our</b> Services</h2>
  <div class="abs title-rule" style="left:517px;top:1439px;width:166px"></div>

  <article class="abs card" style="left:110px">
    <div class="card-photo" style="background:linear-gradient(135deg,#1b3d6e,#5f93c8)" role="img" aria-label="Digital circuit profile of a human head"></div>
    <h3>AI Integration</h3>
    <ul>
      <li>Brevora AI Systems</li>
      <li>Cloudrift Machine Learning (Modelkit, Textlens, Visionbox, ...)</li>
      <li>Skyvault Machine Learning</li>
      <li>Integration with ERP, Financial, Reporting, and many other systems.</li>
    </ul>
    <span class="more">Read More</span>
  </article>

  <article class="abs card" style="left:360px">
    <div class="card-photo" style="background:linear-gradient(135deg,#b9cde3,#e9eef4 50%,#3d6aa3)" role="img" aria-label="White humanoid robot touching a virtual screen"></div>
    <h3>AI Initiation Program</h3>
    <ul>
      <li>Establish AI Initiatives</li>
      <li>Examine Systems &amp; Processes</li>
      <li>Design Learning Algorithms</li>
      <li>Perform Data Analysis</li>
      <li>Interpret Results</li>
      <li>Create Improvement Plans</li>
      <li>Quantify Value Added</li>
    </ul>
    <span class="more">Read More</span>
  </article>

  <article class="abs card" style="left:611px">
    <div class="card-photo" style="background:linear-gradient(135deg,#0d2350,#2f74c8 60%,#0b1d44)" role="img" aria-label="Person working with glowing holographic medical data"></div>
    <h3>Brevora Portals</h3>
    <ul>
      <li>Intelligent Portals</li>
      <li>High Security</li>
      <li>Fully-Controllable Data Integration</li>
    </ul>
    <span class="more">Read More</span>
  </article>

  <article class="abs card" style="left:861px">
    <div class="card-photo" style="background:linear-gradient(180deg,#8b97a8,#c9a77a 55%,#3b3f4a)" role="img" aria-label="City street with skyscrapers at sunset overlaid with data markers"></div>
    <h3>Intelligent Business Systems</h3>
    <ul>
      <li>Production Management</li>
      <li>Operations</li>
      <li>Labor Management</li>
      <li>Inventory Control</li>
      <li>Logistics</li>
    </ul>
    <span class="more">Read More</span>
  </article>
</section>

<section>
  <div class="abs eyebrow" style="left:114px;top:2160px">TEXAS</div>
  <h2 class="abs heading" style="left:114px;top:2186px"><b>About</b> Brevora</h2>
  <div class="abs rule" style="left:114px;top:2236px;width:474px"></div>
  <p class="abs copy" style="left:114px;top:2256px;width:482px">Brevora was founded in Dallas, Texas in 2011 to provide secure, automated customer portal systems for manufacturing companies in the aerospace industry. From a handful of original customers, Brevora Portals has grown to over 400 companies and our personal inter face with a wide variety of businesses has enabled us to grow our technologies into highly intelligent portal systems and beyond.</p>
  <a class="pill navy" style="left:116px;top:2460px;width:201px">View More Info</a>
  <a class="pill dark" style="left:338px;top:2460px;width:202px">Contact Us Now</a>
  <div class="abs photo" style="left:642px;top:2155px;width:447px;height:355px;background:radial-gradient(circle at 55% 50%,#6f9be0,#1f4c96 45%,#0d2656)" role="img" aria-label="Glowing blue brain above a circuit board"></div>
</section>

<section>
  <div class="abs contact-band"></div>
  <h2 class="abs section-title" style="left:0;top:2690px;color:var(--white)"><b>Contact</b> Us</h2>
  <div class="abs title-rule" style="left:523px;top:2738px;width:154px;background:var(--white)"></div>

  <div class="abs field" style="left:208px;top:2773px;width:386px;height:51px">First Name</div>
  <div class="abs field" style="left:606px;top:2773px;width:386px;height:51px">Last Name</div>
  <div class="abs field" style="left:208px;top:2837px;width:386px;height:51px">Email Address</div>
  <div class="abs field" style="left:606px;top:2837px;width:386px;height:51px">Phone Number</div>
  <div class="abs field" style="left:208px;top:2901px;width:386px;height:51px">Company Name</div>
  <div class="abs field" style="left:606px;top:2901px;width:386px;height:51px;justify-content:space-between">Industry
    <svg width="12" height="8" viewBox="0 0 12 8"><path d="M1 1l5 5 5-5" fill="none" stroke="#fff" stroke-width="1.4"/></svg>
  </div>
  <div class="abs field tall" style="left:208px;top:2966px;width:784px;height:89px">Comment or Question</div>
  <a class="pill outline" style="left:500px;top:3076px;width:202px;padding-left:58px">Send Message</a>

  <svg class="abs" style="left:0;top:3195px" width="1200" height="156" viewBox="0 0 1200 156">
    <path d="M0 110Q600 -40 1200 110V156H0Z" fill="var(--charcoal)"/>
  </svg>
  <div class="abs footer-text">Copyrights © 2019.&nbsp; All Rights Reserved.</div>
</section>

</body>
</html>
```